Visitenkarten-Design für Garten- und Landschaftspflege
Tamuga Vent setzte meine Vorstellungen absolut super um ich kann Ihn nur weiter empfehlen. vielen dank
Zielgruppe
Baumpflege, Baumfällung, Garten und Landschaftspflege meine zielgruppe sind Privatpersonen im alter von 20-100Jahren
Aufgabenstellung
Sehr geehrte Damen und Herren, die visitenkarte sollte die angaben so enthalten wie sie auf der von mir gestallteten Visitenkarten sind ( meine ist kein maß der Dinge). Ich habe mein Logo leider nur als 3.jpg Datei. Das Logo darf im Design erändert werden aber bitte nur Feinheiten ansonsten stehen ihnen alle türen offen um kreativ zu sein.
mit freundlichen Grüßen Holger Banzow

```html
<!DOCTYPE html>
<html lang="de">
<head>
<meta charset="utf-8">
<title>Visitenkarten Baumpflege Wernau</title>
<link href="https://fonts.googleapis.com/css2?family=Arimo:wght@400;700&display=swap" rel="stylesheet">
<style>
  :root {
    --leaf: #bdd35f;
    --bark: #2f2f2f;
    --paper: #ffffff;
  }
  * { box-sizing: border-box; margin: 0; padding: 0; }
  html, body { width: 860px; height: 1200px; overflow: hidden; background: var(--paper); }
  body { position: relative; font-family: "Arimo", Arial, sans-serif; color: var(--bark); }

  .card {
    position: absolute; width: 305px; height: 198px;
    background: var(--leaf);
    box-shadow: 3px 4px 6px rgba(0,0,0,0.28);
    overflow: hidden;
  }
  .col-left { left: 98px; }
  .col-right { left: 435px; }
  .row-1 { top: 225px; }
  .row-2 { top: 485px; }
  .row-3 { top: 749px; }

  .stripe { position: absolute; left: 0; right: 0; height: 2px; background: var(--bark); }
  .stripe.top { top: 7px; }
  .stripe.bottom { top: 189px; }
  .stripe-light { position: absolute; left: 0; right: 0; height: 1px; background: var(--paper); }
  .stripe-light.top { top: 3px; }
  .stripe-light.bottom { top: 193px; }

  .brand {
    position: absolute; text-align: center; text-transform: uppercase;
    font-weight: 700; color: var(--bark); letter-spacing: 0.4px;
  }
  .brand-large { left: 0; right: 0; top: 114px; font-size: 13px; line-height: 12px; }
  .brand-small { left: 188px; width: 106px; top: 72px; font-size: 8.5px; line-height: 8px; }
  .brand-bar { left: 0; right: 0; top: 85px; font-size: 10.5px; line-height: 10.5px; }

  .rule { position: absolute; left: 11px; right: 11px; height: 1.5px; background: var(--bark); }
  .rule.upper { top: 82px; }
  .rule.lower { top: 107px; }

  .services { position: absolute; list-style: none; }
  .services li::before { content: "· "; }
  .services-dense { left: 13px; top: 30px; font-size: 7px; line-height: 8.7px; }
  .services-loose { left: 13px; top: 32px; font-size: 8.5px; line-height: 11px; }
  .services-loose .indent { padding-left: 6px; }
  .services-loose .indent::before { content: ""; }
  .services-bottom { left: 101px; top: 118px; font-size: 8.5px; line-height: 10.3px; }

  .person { position: absolute; }
  .person-name { font-size: 13px; letter-spacing: 0.3px; line-height: 1; }
  .person-role { font-size: 5.3px; line-height: 7px; text-align: right; }
  .person-top { left: 13px; top: 125px; }
  .person-bottom { left: 11px; top: 135px; }
  .person-bottom .person-name { font-size: 9.5px; }
  .person-bottom .person-role { text-align: left; line-height: 6px; }

  .contact { position: absolute; font-size: 8.6px; line-height: 11px; }
  .contact-top { left: 160px; top: 125px; }
  .contact-bottom { left: 163px; top: 134px; }
  .contact .line { display: flex; align-items: center; gap: 2px; white-space: nowrap; }
  .contact .indent { padding-left: 12px; }
  .contact .gap { margin-top: 5px; }
  .icon { width: 9px; height: 9px; flex: none; }
</style>
</head>
<body>

<!-- Row 1 -->
<section class="card col-left row-1">
  <div class="stripe-light top"></div><div class="stripe top"></div>
  <div class="brand brand-large">Baumpflege<br>Wernau</div>
  <div class="stripe bottom"></div><div class="stripe-light bottom"></div>
</section>

<section class="card col-right row-1">
  <div class="stripe-light top"></div><div class="stripe top"></div>
  <ul class="services services-dense">
    <li>Neupflanzungen</li>
    <li>Herstellung der Verkehrssicherheit von Bäumen</li>
    <li>Kronenrückschnitt (Einkürzung &amp; Kronenpflege)</li>
    <li>Prüfung von Bäumen auf Standsicherheit</li>
    <li>Fällung von Bäumen</li>
    <li>Obstbaumschnitt</li>
    <li>Wurzelstockfräsen</li>
  </ul>
  <div class="brand brand-small">Baumpflege<br>Wernau</div>
  <div class="person person-top">
    <div class="person-name">Holger Banzow</div>
    <div class="person-role">Fachagrarwirt für Baumpflege<br>&amp; Baumsanierung</div>
  </div>
  <div class="contact contact-top">
    <div class="line"><svg class="icon" viewBox="0 0 10 10"><path d="M5 9.5 C3 6.5 2 5 2 3.6 A3 3 0 0 1 8 3.6 C8 5 7 6.5 5 9.5Z" fill="none" stroke="currentColor" stroke-width="0.9"/><circle cx="5" cy="3.6" r="1" fill="currentColor"/></svg>Lindenweg 4</div>
    <div class="line indent">84120 Moosried</div>
    <div class="line gap"><svg class="icon" viewBox="0 0 10 10"><rect x="3" y="1" width="4" height="8" rx="0.8" fill="currentColor"/></svg>0151 / 482 19 30</div>
    <div class="line"><svg class="icon" viewBox="0 0 10 10"><rect x="0.7" y="2" width="8.6" height="6" fill="none" stroke="currentColor" stroke-width="0.7"/><path d="M0.7 2 L5 5.5 L9.3 2" fill="none" stroke="currentColor" stroke-width="0.7"/></svg>kontakt@baumpflege-wernau.de</div>
    <div class="line"><svg class="icon" viewBox="0 0 10 10"><circle cx="5" cy="5" r="4" fill="none" stroke="currentColor" stroke-width="0.7"/><ellipse cx="5" cy="5" rx="1.8" ry="4" fill="none" stroke="currentColor" stroke-width="0.6"/><path d="M1 5 H9 M1.6 3 H8.4 M1.6 7 H8.4" stroke="currentColor" stroke-width="0.5"/></svg>baumpflege-wernau.de</div>
  </div>
  <div class="stripe bottom"></div><div class="stripe-light bottom"></div>
</section>

<!-- Row 2 -->
<section class="card col-left row-2">
  <div class="stripe-light top"></div><div class="stripe top"></div>
  <div class="brand brand-large">Baumpflege<br>Wernau</div>
  <div class="stripe bottom"></div><div class="stripe-light bottom"></div>
</section>

<section class="card col-right row-2">
  <div class="stripe-light top"></div><div class="stripe top"></div>
  <ul class="services services-loose">
    <li>Neupflanzungen</li>
    <li>Baumschnitt</li>
    <li>Herstellung der Verkehrssicherheit</li>
    <li class="indent">von Bäumen</li>
  </ul>
  <div class="brand brand-small">Baumpflege<br>Wernau</div>
  <div class="person person-top">
    <div class="person-name">Holger Banzow</div>
    <div class="person-role">Fachagrarwirt für Baumpflege<br>&amp; Baumsanierung</div>
  </div>
  <div class="contact contact-top">
    <div class="line"><svg class="icon" viewBox="0 0 10 10"><path d="M5 9.5 C3 6.5 2 5 2 3.6 A3 3 0 0 1 8 3.6 C8 5 7 6.5 5 9.5Z" fill="none" stroke="currentColor" stroke-width="0.9"/><circle cx="5" cy="3.6" r="1" fill="currentColor"/></svg>Lindenweg 4</div>
    <div class="line indent">84120 Moosried</div>
    <div class="line gap"><svg class="icon" viewBox="0 0 10 10"><rect x="3" y="1" width="4" height="8" rx="0.8" fill="currentColor"/></svg>0151 / 482 19 30</div>
    <div class="line"><svg class="icon" viewBox="0 0 10 10"><rect x="0.7" y="2" width="8.6" height="6" fill="none" stroke="currentColor" stroke-width="0.7"/><path d="M0.7 2 L5 5.5 L9.3 2" fill="none" stroke="currentColor" stroke-width="0.7"/></svg>kontakt@baumpflege-wernau.de</div>
    <div class="line"><svg class="icon" viewBox="0 0 10 10"><circle cx="5" cy="5" r="4" fill="none" stroke="currentColor" stroke-width="0.7"/><ellipse cx="5" cy="5" rx="1.8" ry="4" fill="none" stroke="currentColor" stroke-width="0.6"/><path d="M1 5 H9 M1.6 3 H8.4 M1.6 7 H8.4" stroke="currentColor" stroke-width="0.5"/></svg>baumpflege-wernau.de</div>
  </div>
  <div class="stripe bottom"></div><div class="stripe-light bottom"></div>
</section>

<!-- Row 3 -->
<section class="card col-left row-3">
  <div class="rule upper"></div>
  <div class="brand brand-bar">Baumpflege<br>Wernau</div>
  <div class="rule lower"></div>
  <div class="person person-bottom">
    <div class="person-name">Holger Banzow</div>
    <div class="person-role">Fachagrarwirt für Baumpflege<br>&amp; Baumsanierung</div>
  </div>
  <div class="contact contact-bottom">
    <div class="line"><svg class="icon" viewBox="0 0 10 10"><path d="M5 9.5 C3 6.5 2 5 2 3.6 A3 3 0 0 1 8 3.6 C8 5 7 6.5 5 9.5Z" fill="none" stroke="currentColor" stroke-width="0.9"/><circle cx="5" cy="3.6" r="1" fill="currentColor"/></svg>Lindenweg 4</div>
    <div class="line indent">84120 Moosried</div>
    <div class="line gap"><svg class="icon" viewBox="0 0 10 10"><rect x="3" y="1" width="4" height="8" rx="0.8" fill="currentColor"/></svg>0151 / 482 19 30</div>
    <div class="line"><svg class="icon" viewBox="0 0 10 10"><rect x="0.7" y="2" width="8.6" height="6" fill="none" stroke="currentColor" stroke-width="0.7"/><path d="M0.7 2 L5 5.5 L9.3 2" fill="none" stroke="currentColor" stroke-width="0.7"/></svg>kontakt@baumpflege-wernau.de</div>
    <div class="line"><svg class="icon" viewBox="0 0 10 10"><circle cx="5" cy="5" r="4" fill="none" stroke="currentColor" stroke-width="0.7"/><ellipse cx="5" cy="5" rx="1.8" ry="4" fill="none" stroke="currentColor" stroke-width="0.6"/><path d="M1 5 H9 M1.6 3 H8.4 M1.6 7 H8.4" stroke="currentColor" stroke-width="0.5"/></svg>baumpflege-wernau.de</div>
  </div>
</section>

<section class="card col-right row-3">
  <div class="rule upper"></div>
  <div class="brand brand-bar">Baumpflege<br>Wernau</div>
  <div class="rule lower"></div>
  <ul class="services services-bottom">
    <li>Neupflanzungen</li>
    <li>Herstellung der Verkehrssicherheit von Bäumen</li>
    <li>Kronenrückschnitt (Einkürzung &amp; Kronenpflege)</li>
    <li>Prüfung von Bäumen auf Standsicherheit</li>
    <li>Fällung von Bäumen</li>
    <li>Obstbaumschnitt</li>
    <li>Wurzelstockfräsen</li>
  </ul>
</section>

</body>
</html>
```